Criação de Kit com 6 Layouts de Post para Redes Sociais (Facebook, Instagram e etc) para Saúde & Nutrição
" Consultório oftalmológico com ênfase em consultas oftalmológicas, exames complementares e cirurgias oculares "

```html
<!DOCTYPE html>
<html lang="pt-BR">
<head>
<meta charset="UTF-8">
<title>Agendar Consultas – Dra. Helena Marques</title>
<link rel="stylesheet" href="https://fonts.googleapis.com/css2?family=Montserrat:wght@500;600;700;800&family=Cinzel:wght@500&display=swap">
<style>
  :root {
    --navy: #14264d;
    --navy-soft: #1d3363;
    --cream: #fbf6ee;
    --sand: #efe0c4;
    --gold: #c9a66b;
    --skin: #d9b48f;
    --shirt: #bf9a72;
    --white: #ffffff;
  }
  * { margin: 0; padding: 0; box-sizing: border-box; }
  html, body { width: 1200px; height: 1200px; overflow: hidden; background: var(--cream); }
  .post {
    position: relative;
    width: 1200px;
    height: 1200px;
    overflow: hidden;
    font-family: "Montserrat", Arial, sans-serif;
  }
  .scene-photo {
    position: absolute;
    inset: 0;
    background:
      radial-gradient(ellipse 380px 560px at 430px 760px, rgba(191,154,114,0.75), rgba(191,154,114,0) 100%),
      radial-gradient(ellipse 220px 260px at 460px 300px, rgba(217,180,143,0.7), rgba(217,180,143,0) 100%),
      radial-gradient(ellipse 420px 300px at 1080px 820px, rgba(201,166,107,0.45), rgba(201,166,107,0) 100%),
      linear-gradient(100deg, #f4e6cd 0%, #efdcbc 40%, #f7ecdb 70%, #fbf6ee 100%);
  }
  .side-word {
    position: absolute;
    left: 120px;
    top: 0;
    width: 1200px;
    transform-origin: 0 0;
    transform: translateX(150px) rotate(90deg);
    font-weight: 800;
    font-size: 185px;
    line-height: 1;
    letter-spacing: 2px;
    color: rgba(255,255,255,0.82);
    white-space: nowrap;
  }
  .headline {
    position: absolute;
    left: 749px;
    top: 276px;
    width: 293px;
    text-align: center;
    font-weight: 600;
    font-size: 45px;
    color: var(--navy);
    white-space: nowrap;
    letter-spacing: -0.5px;
  }
  .cta-label {
    position: absolute;
    left: 749px;
    width: 293px;
    height: 64px;
    background: var(--navy);
    color: var(--white);
    font-weight: 500;
    font-size: 46px;
    letter-spacing: 1px;
    display: flex;
    align-items: center;
    justify-content: center;
    border-radius: 4px;
  }
  .cta-label.first { top: 340px; }
  .cta-label.second { top: 409px; }
  .contact-button {
    position: absolute;
    left: 749px;
    top: 506px;
    width: 228px;
    height: 52px;
    border-radius: 26px;
    background: var(--navy);
    color: var(--white);
    display: flex;
    align-items: center;
    gap: 14px;
    padding-left: 10px;
    font-weight: 500;
    font-size: 22px;
  }
  .contact-button svg { width: 34px; height: 34px; }
  .signature {
    position: absolute;
    left: 540px;
    top: 960px;
    width: 500px;
    text-align: center;
    font-family: "Cinzel", Georgia, serif;
    font-weight: 500;
    color: var(--navy);
  }
  .signature .name { font-size: 54px; letter-spacing: 1px; white-space: nowrap; }
  .signature .rule { width: 430px; height: 2px; background: var(--gold); margin: 18px auto 16px; }
  .signature .specialty { font-size: 26px; letter-spacing: 11px; }
</style>
</head>
<body>
  <main class="post">
    <div class="scene-photo" role="img" aria-label="Foto de uma jovem sorridente de camiseta bege usando o celular, em consultório claro com tons creme e dourado"></div>

    <div class="side-word" aria-hidden="true">consultas</div>

    <p class="headline">É fácil e rápido</p>
    <div class="cta-label first">AGENDAR</div>
    <div class="cta-label second">CONSULTAS</div>

    <div class="contact-button">
      <svg viewBox="0 0 34 34" aria-hidden="true">
        <circle cx="17" cy="17" r="16" fill="#ffffff"/>
        <path d="M14 10 L21 17 L14 24" fill="none" stroke="#14264d" stroke-width="3.5" stroke-linecap="round" stroke-linejoin="round"/>
      </svg>
      <span>Fale conosco</span>
    </div>

    <div class="signature">
      <div class="name">Dra. Helena Marques</div>
      <div class="rule"></div>
      <div class="specialty">OFTALMOLOGISTA</div>
    </div>
  </main>
</body>
</html>
```